Business card for massage therapy company called Brook Fern Wellness

Need business card for massage therapy company called Brook Fern Wellness. Would like my logo on the front and the back of the card I have 3 options of logos and you can play with what looks better.

Would like this information displayed on the back of the card:

Marcus Ellery
Licensed Massage Therapist
321-555-0147
brookfern-example.com
brookfern_rest_

```html
<!DOCTYPE html>
<html lang="en">
<head>
<meta charset="UTF-8">
<title>Brook Fern Wellness – Business Card</title>
<link rel="stylesheet" href="https://fonts.googleapis.com/css2?family=Montserrat:wght@400;500;700&display=swap">
<style>
  :root {
    --backdrop: #ece6de;
    --card: #ffffff;
    --sage: #737b62;
    --clay: #b8875f;
    --ink: #2b2b2b;
    --shadow: rgba(60, 40, 20, 0.18);
  }
  * { margin: 0; padding: 0; box-sizing: border-box; }
  html, body {
    width: 1200px;
    height: 1200px;
    overflow: hidden;
    background: var(--backdrop);
    font-family: "Montserrat", sans-serif;
  }
  .canvas {
    position: relative;
    width: 1200px;
    height: 1200px;
  }
  .card {
    position: absolute;
    left: 251px;
    width: 697px;
    height: 396px;
    background: var(--card);
    border-radius: 26px;
    box-shadow: 0 6px 18px var(--shadow);
  }
  .card--front { top: 179px; }
  .card--back { top: 625px; }

  .brand {
    position: absolute;
    display: flex;
    align-items: center;
    color: var(--sage);
    font-weight: 500;
    white-space: nowrap;
  }
  .brand__dot {
    border-radius: 50%;
    background: var(--sage);
    flex: none;
  }
  .card--front .brand {
    left: 0;
    right: 0;
    top: 0;
    bottom: 0;
    justify-content: center;
    gap: 18px;
    font-size: 44px;
    letter-spacing: 1px;
  }
  .card--front .brand__dot { width: 22px; height: 22px; }

  .card--back .brand {
    left: 40px;
    top: 182px;
    width: 252px;
    justify-content: center;
    gap: 8px;
    font-size: 19px;
  }
  .card--back .brand__dot { width: 10px; height: 10px; }

  .divider {
    position: absolute;
    left: 331px;
    top: 113px;
    width: 2px;
    height: 171px;
    background: var(--sage);
  }
  .contact {
    position: absolute;
    left: 364px;
    top: 108px;
  }
  .contact__name {
    color: var(--sage);
    font-weight: 700;
    font-size: 33px;
    letter-spacing: 0.5px;
    line-height: 1.2;
    text-transform: uppercase;
  }
  .contact__role {
    color: var(--clay);
    font-weight: 400;
    font-size: 18px;
    letter-spacing: 0.6px;
    margin-top: 2px;
  }
  .contact__list {
    list-style: none;
    margin-top: 34px;
    color: var(--ink);
    font-size: 17.5px;
    font-weight: 400;
    line-height: 29px;
    letter-spacing: 0.3px;
  }
</style>
</head>
<body>
<main class="canvas">
  <section class="card card--front" aria-label="Card front">
    <div class="brand">
      <span class="brand__dot"></span>
      <span class="brand__name">Brook Fern Wellness</span>
    </div>
  </section>

  <section class="card card--back" aria-label="Card back">
    <div class="brand">
      <span class="brand__dot"></span>
      <span class="brand__name">Brook Fern Wellness</span>
    </div>
    <div class="divider"></div>
    <div class="contact">
      <h1 class="contact__name">Marcus Ellery</h1>
      <p class="contact__role">Licensed Massage Therapist</p>
      <ul class="contact__list">
        <li>321-555-0147</li>
        <li>brookfern-example.com</li>
        <li>brookfern_rest_</li>
      </ul>
    </div>
  </section>
</main>
</body>
</html>
```